Professional Website for Leading Global Private Equity Real Estate Company

The company is a leading global Private Equity Real Estate (PERE). We need a homepage design, an inner page design, and color/font tweaks to the logo (color should be more soothing than current blue used in the logo). The logo website should project the company as global, professional, experienced, trustworthy, accessible, YOUNG, DYNAMIC, hi-tech. PLEASE SEE the attached Design Brief Word Doc for details.

Target Market(s)

institional investors and wealthy private individuals

Industry/Entity Type

Finance

Number of Pages Required

2 page

Font styles to use
Sans Serif
Other font styles liked:
• either like in https://www.harrowfield.com/ or like in presentations (Montserrat Black & Montserrat Light, Century Gothic, Blair ITC, Almoni Neue DL 4.0 AAA Medium, Almoni DL AAA)

Requirements
Must have
• new color palette that is NOT based on current logo. they want a more soothing color palette than the blue in that logo. the new color palette should project: global, professional, experienced, trustworthy, accessible, YOUNG, DYNAMIC, hi-tech.
Nice to have
• the likes these sites: https://www.harrowfield.com/ and https://www.kvt.law/

```html
<!DOCTYPE html>
<html lang="en">
<head>
<meta charset="utf-8">
<title>Veranor Real Estate</title>
<link href="https://fonts.googleapis.com/css2?family=Montserrat:wght@300;400;600;700;800;900&family=Open+Sans:wght@400;600;700&display=swap" rel="stylesheet">
<style>
:root{
  --teal:#4aa7c6;
  --teal-dark:#3892b1;
  --teal-light:#e6f3f8;
  --ink:#1e1e1e;
  --dark:#222426;
  --darker:#17191a;
  --white:#ffffff;
  --grey:#6c6f73;
  --line:#d8dde0;
}
*{margin:0;padding:0;box-sizing:border-box}
html,body{width:1200px;height:4132px;overflow:hidden}
body{position:relative;font-family:"Open Sans",Arial,sans-serif;color:var(--ink);background:var(--white)}
.abs{position:absolute}
h2,h3,h4,.nav a,.btn,.logo{font-family:"Montserrat",Arial,sans-serif}
p{font-size:13px;line-height:1.7}
.btn{display:inline-block;background:var(--teal);color:var(--white);font-size:11px;font-weight:700;letter-spacing:.5px;text-transform:uppercase;border-radius:20px;padding:8px 22px}
.btn.small{padding:6px 16px;font-size:10px}
.btn.ghost{background:var(--white);color:var(--teal)}
.photo{background:linear-gradient(160deg,#c9d8e2,#8ea3b1 55%,#5f6e78);border-radius:26px}

/* header */
.topbar{left:0;top:0;width:1200px;height:32px;background:var(--darker);color:#cfd3d6;font-size:11px;display:flex;align-items:center;gap:24px;padding-left:150px}
.topbar span{display:flex;align-items:center;gap:6px}
.nav{left:0;top:32px;width:1200px;height:48px;background:rgba(20,22,24,.85);display:flex;align-items:center;padding:0 150px}
.logo{display:flex;align-items:center;gap:8px;color:var(--white);font-weight:700;font-size:15px;letter-spacing:1px;text-transform:uppercase}
.logo i{width:18px;height:18px;border-radius:50%;background:var(--teal);display:block}
.nav ul{margin-left:auto;display:flex;gap:30px;list-style:none;align-items:center}
.nav a{color:var(--white);font-size:11px;font-weight:600;text-decoration:none}
.nav a.active{color:var(--teal)}
.hero{left:0;top:0;width:1200px;height:560px;background:linear-gradient(180deg,#2c2a2b 0%,#6d5a49 35%,#9a8068 55%,#3c3d40 100%)}
.play{left:570px;top:250px}

/* about */
.about-photo{left:160px;top:628px;width:340px;height:332px}
.about-text{left:548px;top:680px;width:612px}
h2.title{font-size:36px;font-weight:800;text-transform:uppercase;letter-spacing:.5px}
.about-text p{color:var(--grey);margin-top:14px}

/* platforms */
.platforms{left:0;top:1020px;width:1200px;height:440px;background:var(--teal)}
.platforms .wave{left:0;top:0}
.plat-head{left:0;top:1048px;width:1200px;text-align:center;color:var(--white)}
.plat-head h3{font-size:22px;font-weight:400;text-transform:uppercase}
.plat-head h2{font-size:38px;font-weight:800;text-transform:uppercase;line-height:1}
.plat{top:1156px;width:160px;text-align:center;color:var(--white)}
.plat .circ{width:150px;height:150px;margin:0 auto;border-radius:50%;border:5px solid var(--white);background:linear-gradient(160deg,#d6dfe5,#8e9faa)}
.plat h4{font-size:12px;font-weight:700;margin-top:16px;text-transform:uppercase}
.plat p{font-size:11px;line-height:1.5;margin:6px 0 14px}

/* cards */
.band{left:0;top:1604px;width:215px;height:92px;background:var(--ink)}
.card-img{width:200px;height:192px}
.card-text{width:210px}
.card-text h4{font-size:15px;font-weight:700;text-transform:uppercase}
.card-text p{font-size:11px;line-height:1.55;color:var(--grey);margin:8px 0 12px}

/* edge */
.edge{left:0;top:2240px;width:1200px;height:448px;background:linear-gradient(90deg,#2a2c2e,#1b1d1e)}
.edge-photo{left:160px;top:2308px;width:340px;height:320px}
.edge-text{left:548px;top:2330px;width:612px;color:var(--white)}
.edge-text p{color:#d7dadc;margin-top:14px}

/* newsletter */
.stay{left:0;top:2730px;width:1200px;text-align:center}
.subscribe{left:260px;top:2812px;width:500px;height:52px;border:2px solid var(--teal);border-radius:26px;padding-left:26px;display:flex;align-items:center;font-size:12px;color:#9aa0a4}
.subscribe-btn{left:772px;top:2812px;width:140px;height:52px;border-radius:26px;font-size:15px;display:flex;align-items:center;justify-content:center;padding:0}

/* responsibility */
.resp-photo{left:0;top:2940px;width:480px;height:460px;background:linear-gradient(170deg,#cfe2ef,#e9ecee 45%,#8fa56d 85%);border-radius:0}
.resp-panel{left:488px;top:2920px;width:712px;height:480px;background:var(--teal);border-radius:40px 0 0 40px;padding:62px 80px 0 80px;color:var(--white)}
.resp-panel p{margin-top:14px;color:#eef7fa}

/* contact */
.contact{left:0;top:3400px;width:1200px;height:460px;background:linear-gradient(180deg,#2c2e31,#1d1f21)}
.contact-head{left:0;top:3424px;width:1200px;text-align:center;color:var(--white)}
.contact-head h4{font-size:14px;font-weight:600;text-transform:uppercase}
.contact-head h2{font-size:44px;font-weight:800;text-transform:uppercase;line-height:1.1}
.field{border-bottom:1px solid #7b7f83;color:#c5c9cc;font-size:12px;padding-bottom:8px}
.submit{left:508px;top:3700px;width:184px;height:40px;border-radius:20px;font-size:14px;display:flex;align-items:center;justify-content:center;padding:0}

/* footer */
.footer{left:0;top:3860px;width:1200px;height:272px;background:var(--darker);color:#c9cdd0}
.foot-col h4{font-size:14px;font-weight:700;color:var(--white);text-transform:uppercase}
.foot-col h4 span{color:var(--teal)}
.foot-col ul{list-style:none;margin-top:12px}
.foot-col li{font-size:11px;line-height:2}
.foot-col li::before{content:"›  ";color:var(--teal)}
.info{display:flex;gap:8px;font-size:11px;line-height:1.6;margin-top:12px}
.social{display:flex;gap:8px;margin-top:14px}
.social i{display:block;width:22px;height:22px;border-radius:50%;border:1px solid #7b7f83}
.copy{left:0;top:4100px;width:1200px;height:32px;background:var(--teal);color:var(--white);font-size:10px;display:flex;align-items:center;justify-content:center;letter-spacing:.5px}
</style>
</head>
<body>

<!-- hero -->
<div class="abs hero" role="img" aria-label="City skyline with residential towers at dusk"></div>
<svg class="abs play" width="60" height="60" viewBox="0 0 60 60"><circle cx="30" cy="30" r="28" fill="rgba(255,255,255,.35)"/><path d="M24 18 L42 30 L24 42 Z" fill="#fff"/></svg>

<div class="abs topbar">
  <span><svg width="11" height="11" viewBox="0 0 24 24"><path fill="#4aa7c6" d="M6.6 10.8a15 15 0 0 0 6.6 6.6l2.2-2.2c.3-.3.7-.4 1-.2 1.1.4 2.3.6 3.6.6.6 0 1 .4 1 1V20c0 .6-.4 1-1 1A17 17 0 0 1 3 4c0-.6.4-1 1-1h3.5c.6 0 1 .4 1 1 0 1.3.2 2.5.6 3.6.1.3 0 .7-.2 1z"/></svg>+1 555 014 2207</span>
  <span><svg width="12" height="10" viewBox="0 0 24 18"><rect x="1" y="1" width="22" height="16" rx="2" fill="none" stroke="#4aa7c6" stroke-width="2"/><path d="M1 2l11 8 11-8" fill="none" stroke="#4aa7c6" stroke-width="2"/></svg>hello@veranor-re.com</span>
</div>
<nav class="abs nav">
  <div class="logo"><i></i>Veranor Real Estate</div>
  <ul>
    <li><a class="active">Home</a></li>
    <li><a>About Us</a></li>
    <li><a>Our Business</a></li>
    <li><a>Investors Lobby</a></li>
    <li><a>News</a></li>
    <li><a>Contact Us</a></li>
    <li><span class="btn small">Log In</span></li>
  </ul>
</nav>

<!-- about -->
<div class="abs photo about-photo" role="img" aria-label="Modern apartment building with balconies"></div>
<div class="abs about-text">
  <h2 class="title">About Us</h2>
  <p>Lorem ipsum dolor sit amet, consectetur adipiscing elit. Vestibulum id sollicitudin diam. Aliquam ut tincidunt leo. Vivamus molestie sapien id posuere lacinia. In consectetur ut leo quis vehicula. Maecenas in mollis eu tempor. Mauris mollis ultrices diam. Donec sollicitudin, ipsum et mattis posuere, ipsum lorem lacinia odio, sed dictum ultrices a. Morbi a rhoncus enim. Aenean fringilla lectus ut odio suscipit. Sed sollicitudin nec in porta dictum maximus.</p>
  <p>In bibendum lacus lacus at enim dui. Cras in pharetra magna. Phasellus tincidunt enim ante, id volutpat tellus ultricies a. Morbi a rhoncus enim. Aenean fringilla lectus ut odio suscipit. Sed sollicitudin nec in porta dictum maximus.</p>
  <p style="margin-top:26px"><span class="btn">Read More</span></p>
</div>

<!-- platforms -->
<div class="abs platforms"></div>
<svg class="abs" style="left:0;top:1020px" width="1200" height="440" viewBox="0 0 1200 440"><path d="M0 0 H700 C560 60 420 40 300 140 C200 220 80 230 0 260 Z" fill="#56b1cf" opacity=".6"/></svg>
<div class="abs plat-head"><h3>Our Investment</h3><h2>Platforms</h2></div>
<div class="abs plat" style="left:152px"><div class="circ" role="img" aria-label="Apartment tower"></div><h4>Lorem Ipsum Dolo</h4><p>Lorem ipsum dolor sit amet consectetur adipiscing elit sed do</p><span class="btn small ghost">Read More</span></div>
<div class="abs plat" style="left:342px"><div class="circ" role="img" aria-label="Professionals in a meeting"></div><h4>Lorem Ipsum Dolo</h4><p>Lorem ipsum dolor sit amet consectetur adipiscing elit sed do</p><span class="btn small ghost">Read More</span></div>
<div class="abs plat" style="left:520px"><div class="circ" role="img" aria-label="Residential complex"></div><h4>Lorem Ipsum Dolo</h4><p>Lorem ipsum dolor sit amet consectetur adipiscing elit sed do</p><span class="btn small ghost">Read More</span></div>
<div class="abs plat" style="left:698px"><div class="circ" role="img" aria-label="Handshake over a house model"></div><h4>Lorem Ipsum Dolo</h4><p>Lorem ipsum dolor sit amet consectetur adipiscing elit sed do</p><span class="btn small ghost">Read More</span></div>
<div class="abs plat" style="left:876px"><div class="circ" role="img" aria-label="Family at home"></div><h4>Lorem Ipsum Dolo</h4><p>Lorem ipsum dolor sit amet consectetur adipiscing elit sed do</p><span class="btn small ghost">Read More</span></div>

<!-- cards -->
<div class="abs band"></div>
<div class="abs photo card-img" style="left:160px;top:1560px" role="img" aria-label="Couple standing by a home"></div>
<div class="abs card-text" style="left:380px;top:1576px"><h4>Lorem Ipsum Dolor</h4><p>Lorem ipsum dolor sit amet, consectetur adipiscing elit. Vestibulum id sollicitudin diam. Aliquam ut tincidunt leo. Vivamus molestie sapien id.</p><span class="btn small">Read More</span></div>
<div class="abs photo card-img" style="left:622px;top:1560px" role="img" aria-label="Suburban houses"></div>
<div class="abs card-text" style="left:840px;top:1576px"><h4>Lorem Ipsum Dolor</h4><p>Lorem ipsum dolor sit amet, consectetur adipiscing elit. Vestibulum id sollicitudin diam. Aliquam ut tincidunt leo. Vivamus molestie sapien id.</p><span class="btn small">Read More</span></div>
<div class="abs photo card-img" style="left:160px;top:1780px" role="img" aria-label="Agent holding house keys"></div>
<div class="abs card-text" style="left:380px;top:1796px"><h4>Lorem Ipsum Dolor</h4><p>Lorem ipsum dolor sit amet, consectetur adipiscing elit. Vestibulum id sollicitudin diam. Aliquam ut tincidunt leo. Vivamus molestie sapien id.</p><span class="btn small">Read More</span></div>
<div class="abs photo card-img" style="left:622px;top:1780px" role="img" aria-label="Colourful apartment facade"></div>
<div class="abs card-text" style="left:840px;top:1796px"><h4>Lorem Ipsum Dolor</h4><p>Lorem ipsum dolor sit amet, consectetur adipiscing elit. Vestibulum id sollicitudin diam. Aliquam ut tincidunt leo. Vivamus molestie sapien id.</p><span class="btn small">Read More</span></div>
<div class="abs photo card-img" style="left:432px;top:2000px" role="img" aria-label="Modern villa at dusk"></div>
<div class="abs card-text" style="left:652px;top:2016px"><h4>Lorem Ipsum Dolor</h4><p>Lorem ipsum dolor sit amet, consectetur adipiscing elit. Vestibulum id sollicitudin diam. Aliquam ut tincidunt leo. Vivamus molestie sapien id.</p><span class="btn small">Read More</span></div>

<!-- edge -->
<div class="abs edge" role="img" aria-label="Dark city background"></div>
<div class="abs photo edge-photo" role="img" aria-label="Apartment building with balconies"></div>
<div class="abs edge-text">
  <h2 class="title">Our Edge</h2>
  <p>Lorem ipsum dolor sit amet, consectetur adipiscing elit. Vestibulum id sollicitudin diam. Aliquam ut tincidunt leo. Vivamus molestie sapien id posuere lacinia. In consectetur ut leo quis vehicula. Maecenas in mollis eu tempor. Mauris mollis ultrices diam. Donec sollicitudin, ipsum et mattis posuere, ipsum lorem lacinia odio, sed dictum ultrices a. Morbi a rhoncus enim. Aenean fringilla lectus ut odio suscipit. Sed sollicitudin nec in porta dictum maximus.</p>
  <p>In bibendum lacus lacus at enim dui. Cras in pharetra magna. Phasellus tincidunt enim ante, id volutpat tellus ultricies a. Morbi a rhoncus enim. Aenean fringilla lectus ut odio suscipit. Sed sollicitudin nec in porta dictum maximus.</p>
  <p style="margin-top:26px"><span class="btn">Read More</span></p>
</div>

<!-- newsletter -->
<div class="abs stay"><h2 class="title">Stay Updated</h2></div>
<div class="abs subscribe">Enter Your Email</div>
<div class="abs btn subscribe-btn">Submit</div>

<!-- responsibility -->
<div class="abs photo resp-photo" role="img" aria-label="White apartment block with lawn"></div>
<div class="abs resp-panel">
  <h2 class="title">Our Responsibility</h2>
  <p>Lorem ipsum dolor sit amet, consectetur adipiscing elit. Vestibulum id sollicitudin diam. Aliquam ut tincidunt leo. Vivamus molestie sapien id posuere lacinia. In consectetur ut leo quis vehicula. Maecenas in mollis eu tempor. Mauris mollis ultrices diam. Donec sollicitudin, ipsum et mattis posuere, ipsum lorem lacinia odio, sed dictum ultrices a. Morbi a rhoncus enim. Aenean fringilla lectus ut odio suscipit.</p>
  <p>In bibendum lacus lacus at enim dui. Cras in pharetra magna. Phasellus tincidunt enim ante, id volutpat tellus ultricies a. Morbi a rhoncus enim. Sed sollicitudin nec in porta dictum maximus.</p>
  <p style="margin-top:26px"><span class="btn ghost">Read More</span></p>
</div>

<!-- contact -->
<div class="abs contact" role="img" aria-label="Dark city skyline background"></div>
<div class="abs contact-head"><h4>Get In Touch</h4><h2>Contact Us</h2></div>
<div class="abs field" style="left:212px;top:3524px;width:356px">Name</div>
<div class="abs field" style="left:592px;top:3524px;width:356px">Phone</div>
<div class="abs field" style="left:212px;top:3580px;width:736px">Email</div>
<div class="abs field" style="left:212px;top:3632px;width:736px;height:56px">Message</div>
<div class="abs btn submit">Submit</div>

<!-- footer -->
<div class="abs footer"></div>
<div class="abs foot-col" style="left:200px;top:3880px;width:280px">
  <div class="logo" style="font-size:13px"><i></i>Veranor Real Estate</div>
  <p style="font-size:11px;line-height:1.6;margin-top:12px;color:#c9cdd0">Lorem ipsum dolor sit amet, consectetur adipiscing elit. Vestibulum id sollicitudin diam. Aliquam ut tincidunt leo. Vivamus molestie sapien lacinia.</p>
</div>
<div class="abs foot-col" style="left:516px;top:3880px;width:200px">
  <h4>Important <span>Links</span></h4>
  <ul><li>Home</li><li>About Us</li><li>Our Business</li><li>Investors Lobby</li><li>News</li><li>Contact Us</li></ul>
</div>
<div class="abs foot-col" style="left:744px;top:3880px;width:260px">
  <h4>Contact <span>Details</span></h4>
  <div class="info"><svg width="12" height="14" viewBox="0 0 24 28"><path fill="#4aa7c6" d="M12 0a10 10 0 0 0-10 10c0 7 10 18 10 18s10-11 10-18A10 10 0 0 0 12 0zm0 14a4 4 0 1 1 0-8 4 4 0 0 1 0 8z"/></svg><span>48 Harbor Crest Ave, Suite 210,<br>Lakeport, FL 30000</span></div>
  <div class="info"><svg width="12" height="12" viewBox="0 0 24 24"><path fill="#4aa7c6" d="M6.6 10.8a15 15 0 0 0 6.6 6.6l2.2-2.2c.3-.3.7-.4 1-.2 1.1.4 2.3.6 3.6.6.6 0 1 .4 1 1V20c0 .6-.4 1-1 1A17 17 0 0 1 3 4c0-.6.4-1 1-1h3.5c.6 0 1 .4 1 1 0 1.3.2 2.5.6 3.6.1.3 0 .7-.2 1z"/></svg><span>+1 555 014 2207</span></div>
  <div class="info"><svg width="12" height="10" viewBox="0 0 24 18"><rect x="1" y="1" width="22" height="16" rx="2" fill="none" stroke="#4aa7c6" stroke-width="2"/><path d="M1 2l11 8 11-8" fill="none" stroke="#4aa7c6" stroke-width="2"/></svg><span>hello@veranor-re.com</span></div>
  <div class="social"><i></i><i></i><i></i><i></i></div>
</div>
<div class="abs copy">Copyright © 2024 Veranor Real Estate. All Rights Reserved.</div>

</body>
</html>
```